Need Bus charter business website,

I am starting a bus charter business in the near future. I am based in Geelong, Victoria in Australia. I will have a 25 or 28 seater bus that will be used to take people on charted trips. Whether they be to birthday parties, weddings, sporting events, corporate events, mystery trips, going down the Great Ocean Road, or anywhere someone wants. As for colour scheme, I'm leaning towards something blue and grey, but open to anything really that catches my eye. I played around with a basic web design program and made a basic site which I uploaded ( www.kelmoride.com.au) It has things which I wanted to include such as, services I will provide, trip information, contact form etc.

I don't mind if the layout is completely different to my site as it was only a template that was included in the program I used. I would like the overall design to be relatively fluid, not having to back-track a lot to navigate the site.

```html
<!DOCTYPE html>
<html lang="en">
<head>
<meta charset="utf-8">
<title>Bayline Coach Tours</title>
<link href="https://fonts.googleapis.com/css2?family=Roboto:wght@300;400;500;700&family=Open+Sans:wght@400;600;700&display=swap" rel="stylesheet">
<style>
:root{
  --blue:#0a78d6;
  --blue-dark:#0563b4;
  --ink:#1f1f1f;
  --text:#333;
  --muted:#666;
  --panel:#f4f4f4;
  --field:#ececec;
  --field-text:#9a9a9a;
  --band:#f8f8f8;
  --hero-dark:#151515;
  --white:#fff;
}
*{box-sizing:border-box;margin:0;padding:0}
html,body{width:1120px;height:1200px;overflow:hidden;background:var(--white)}
body{position:relative;font-family:"Roboto",sans-serif;color:var(--text)}
.abs{position:absolute}

/* navigation */
.main-nav{left:161px;top:9px;width:800px;height:40px;border-bottom:2px solid var(--ink);display:flex;justify-content:space-between}
.nav-item{display:flex;align-items:center;gap:11px;height:30px;font-size:14px;color:var(--ink)}
.nav-icon{width:28px;height:28px;border-radius:50%;background:var(--blue);display:flex;align-items:center;justify-content:center}

/* brand row */
.brand-name{left:162px;top:76px;font-family:"Roboto",sans-serif;font-size:30px;font-weight:400;color:var(--ink);letter-spacing:.5px}
.social-top{left:812px;top:88px;display:flex;gap:12px}
.social-top span{width:28px;height:25px;border-bottom:2px solid var(--ink);display:flex;justify-content:center}
.social-top span i{display:block;width:10px;height:10px;border-radius:50%;background:var(--ink);margin-top:5px}

/* hero */
.hero{left:161px;top:158px;width:800px;height:260px;background:radial-gradient(circle at 30% 40%,#3a3a3a 0,#1c1c1c 55%,var(--hero-dark) 100%)}
.hero-kicker{left:188px;top:231px;font-size:24px;font-weight:300;color:var(--white);letter-spacing:.3px}
.hero-title{left:187px;top:254px;font-size:38px;font-weight:700;color:var(--white);letter-spacing:.5px}
.btn{display:flex;align-items:center;justify-content:center;background:linear-gradient(#0d80e0,var(--blue-dark));color:var(--white);font-family:"Open Sans",sans-serif;font-weight:600;font-size:11px}
.hero-btn{left:187px;top:302px;width:114px;height:43px}
.dots{left:188px;top:393px;display:flex;gap:4px}
.dots i{width:8px;height:8px;border-radius:50%;background:#555}
.dots i:first-child{background:var(--white)}
.hero-coach{left:528px;top:148px;width:434px;height:292px;border-radius:60px 20px 10px 40px;background:linear-gradient(160deg,#e9eaec 0%,#c9ccd0 45%,#2a2a2a 46%,#1a1a1a 60%,#d8dadd 61%,#b7babe 100%)}

/* booking */
.booking{left:161px;top:418px;width:355px;height:315px;background:var(--panel)}
.booking-title{left:187px;top:431px;font-size:32px;color:var(--blue);font-weight:400}
.field-label{font-size:12.5px;color:var(--ink)}
.field{width:148px;height:32px;background:var(--field);font-size:10px;color:var(--field-text);display:flex;align-items:center;justify-content:space-between;padding:0 10px 0 12px}
.book-now{left:161px;top:733px;width:355px;height:47px;font-family:"Roboto",sans-serif;font-size:17px;font-weight:400}

/* welcome */
.welcome-title{left:547px;top:481px;width:414px;white-space:nowrap;font-size:23px;color:var(--blue);font-weight:300}
.welcome-title b{font-weight:400}
.photo{top:518px;height:107px;width:134px}
.welcome-text{left:549px;top:635px;width:412px;font-family:"Open Sans",sans-serif;font-size:10.5px;line-height:15px;color:var(--muted);letter-spacing:-.1px}
.welcome-btn{left:549px;top:686px;width:105px;height:40px}

/* trip band */
.trip-band{left:0;top:797px;width:1120px;height:270px;background:var(--band)}
.traveller-left{left:170px;top:815px;width:140px;height:234px;border-radius:40px 40px 10px 10px;background:linear-gradient(#8a6a55,#3a4f79 55%,#c8202c)}
.traveller-right{left:745px;top:722px;width:215px;height:336px;border-radius:50px 50px 10px 10px;background:linear-gradient(#f1f1f1,#e3e3e3 45%,#2b2b2b 70%,#2c3a5c)}
.trip-title{left:366px;top:857px;font-size:32px;color:var(--blue);font-weight:400}
.trip-text{left:366px;top:906px;width:350px;font-family:"Open Sans",sans-serif;font-size:11.6px;line-height:15px;color:var(--ink);letter-spacing:-.1px}
.trip-btn{left:366px;top:960px;width:106px;height:40px}

/* footer */
.footer-brand{left:161px;top:1088px;width:800px;height:50px;display:flex;align-items:center;justify-content:flex-end;gap:12px;border-bottom:2px solid var(--ink)}
.footer-brand .mark{width:22px;height:22px;background:var(--blue)}
.footer-brand span{font-size:24px;color:var(--ink)}
.footer-bar{left:0;top:1152px;width:1120px;height:48px;background:var(--blue)}
.copyright{left:162px;top:1169px;font-family:"Open Sans",sans-serif;font-size:12.5px;font-weight:600;color:var(--white)}
.social-foot{left:822px;top:1169px;display:flex;gap:26px}
.social-foot i{width:14px;height:14px;border-radius:50%;background:var(--white)}
</style>
</head>
<body>

<nav class="main-nav abs">
  <div class="nav-item"><span class="nav-icon"><svg width="14" height="14" viewBox="0 0 14 14"><path d="M1 7 7 1l6 6M3 6v7h8V6" fill="none" stroke="#fff" stroke-width="1.6"/></svg></span>Home</div>
  <div class="nav-item"><span class="nav-icon"><svg width="14" height="14" viewBox="0 0 14 14"><circle cx="7" cy="7" r="6" fill="none" stroke="#fff" stroke-width="1.5"/><path d="M7 6v5M7 3.5v1" stroke="#fff" stroke-width="1.6"/></svg></span>About</div>
  <div class="nav-item"><span class="nav-icon"><svg width="14" height="14" viewBox="0 0 14 14"><rect x="1" y="2" width="10" height="11" fill="none" stroke="#fff" stroke-width="1.4"/><path d="M5 9l7-7" stroke="#fff" stroke-width="1.8"/></svg></span>Book A Trip</div>
  <div class="nav-item"><span class="nav-icon"><svg width="14" height="14" viewBox="0 0 14 14"><circle cx="7" cy="6" r="3.5" fill="none" stroke="#fff" stroke-width="1.5"/><path d="M5.5 11h3M7 0v1M1 6h1M12 6h1" stroke="#fff" stroke-width="1.4"/></svg></span>Services</div>
  <div class="nav-item"><span class="nav-icon"><svg width="14" height="14" viewBox="0 0 14 14"><path d="M3 1l3 3-2 2c1 2 2 3 4 4l2-2 3 3-2 2C6 13 1 8 1 3z" fill="#fff"/></svg></span>Contact</div>
  <div class="nav-item"><span class="nav-icon"><svg width="14" height="14" viewBox="0 0 14 14"><path d="M1 1h6l6 6-6 6-6-6z" fill="none" stroke="#fff" stroke-width="1.5"/><circle cx="4" cy="4" r="1.2" fill="#fff"/></svg></span>Trips On Offers</div>
</nav>

<div class="brand-name abs">Bayline Coach Tours</div>
<div class="social-top abs" aria-label="Social links"><span><i></i></span><span><i></i></span><span><i></i></span><span><i></i></span></div>

<section class="hero abs"></section>
<div class="hero-kicker abs">MAKING TRANSPORTATION</div>
<div class="hero-title abs">FAST AND SAFE !</div>
<div class="btn hero-btn abs">READ MORE</div>
<div class="dots abs"><i></i><i></i><i></i></div>
<div class="hero-coach abs" role="img" aria-label="Photo of a white luxury touring coach"></div>

<section class="booking abs"></section>
<h2 class="booking-title abs">BOOK MY BUS</h2>

<div class="field-label abs" style="left:190px;top:478px">FROM</div>
<div class="field-label abs" style="left:341px;top:478px">TO</div>
<div class="field abs" style="left:188px;top:498px">SELECT<svg width="9" height="6" viewBox="0 0 9 6"><path d="M1 1l3.5 3.5L8 1" fill="none" stroke="#999" stroke-width="1.2"/></svg></div>
<div class="field abs" style="left:340px;top:498px">SELECT<svg width="9" height="6" viewBox="0 0 9 6"><path d="M1 1l3.5 3.5L8 1" fill="none" stroke="#999" stroke-width="1.2"/></svg></div>

<div class="field-label abs" style="left:190px;top:543px">DEPART ON</div>
<div class="field-label abs" style="left:341px;top:543px">PASSENGERS</div>
<div class="field abs" style="left:188px;top:561px">05-05-2015<svg width="9" height="12" viewBox="0 0 9 12"><path d="M1 4.5 4.5 1 8 4.5M1 7.5 4.5 11 8 7.5" fill="none" stroke="#999" stroke-width="1.2"/></svg></div>
<div class="field abs" style="left:340px;top:561px">05<svg width="9" height="12" viewBox="0 0 9 12"><path d="M1 4.5 4.5 1 8 4.5M1 7.5 4.5 11 8 7.5" fill="none" stroke="#999" stroke-width="1.2"/></svg></div>

<div class="field-label abs" style="left:190px;top:606px">SITTING OPTION</div>
<div class="field-label abs" style="left:341px;top:606px">MORE OPTION</div>
<div class="field abs" style="left:188px;top:624px">ANY<svg width="9" height="6" viewBox="0 0 9 6"><path d="M1 1l3.5 3.5L8 1" fill="none" stroke="#999" stroke-width="1.2"/></svg></div>
<div class="field abs" style="left:340px;top:624px">SELECT<svg width="9" height="6" viewBox="0 0 9 6"><path d="M1 1l3.5 3.5L8 1" fill="none" stroke="#999" stroke-width="1.2"/></svg></div>

<div class="field-label abs" style="left:190px;top:670px">DEPARTURE TIME</div>
<div class="field-label abs" style="left:341px;top:670px">BUS TYPE</div>
<div class="field abs" style="left:188px;top:688px">ANY TIME<svg width="9" height="6" viewBox="0 0 9 6"><path d="M1 1l3.5 3.5L8 1" fill="none" stroke="#999" stroke-width="1.2"/></svg></div>
<div class="field abs" style="left:340px;top:688px">ANY BUS<svg width="9" height="6" viewBox="0 0 9 6"><path d="M1 1l3.5 3.5L8 1" fill="none" stroke="#999" stroke-width="1.2"/></svg></div>

<div class="btn book-now abs">BOOK NOW !</div>

<h2 class="welcome-title abs">WELCOME TO <b>BAYLINE COACH TOURS:</b></h2>
<div class="photo abs" style="left:549px;background:linear-gradient(#5d9ee0,#d6e6f4 55%,#e8ecef)" role="img" aria-label="Photo of a white coach under a blue sky"></div>
<div class="photo abs" style="left:689px;background:linear-gradient(#6f9a52,#c4c9c2 50%,#8a8a80)" role="img" aria-label="Photo of guests gathered beside a coach among trees"></div>
<div class="photo abs" style="left:828px;background:linear-gradient(#cbbfae,#d9d5cf 40%,#7d6e62)" role="img" aria-label="Photo of passengers boarding a coach in a street"></div>
<p class="welcome-text abs">We are an accredited bus company that operates bus trip and charter work in the Geelong area. We offer a range of services, from day trips down the Great Ocean Road, to transport for wedding guests, Buck’s and Hen’s nights or school trips.</p>
<div class="btn welcome-btn abs">READ MORE</div>

<section class="trip-band abs"></section>
<div class="traveller-left abs" role="img" aria-label="Photo of a traveller with a red suitcase"></div>
<div class="traveller-right abs" role="img" aria-label="Photo of a waving traveller with a navy suitcase"></div>
<h2 class="trip-title abs">WANT TO BOOK A TRIP?</h2>
<p class="trip-text abs">Check out our trips we are currently offering here or if you have an idea or location in mind, contact us here and we’ll do our best to make it happen</p>
<div class="btn trip-btn abs">READ MORE</div>

<div class="footer-brand abs"><i class="mark"></i><span>Bayline Coach Tours</span></div>
<footer class="footer-bar abs"></footer>
<div class="copyright abs">Copyright 2014 Bayline Coach Tours Pty Ltd. ACN: 412 305 887</div>
<div class="social-foot abs" aria-label="Social links"><i></i><i></i><i></i><i></i></div>

</body>
</html>
```